Luxurious Chocolate Box range for Varden + Pruitt Chocolate

New luxurious indulgent chocolate box packaging for Varden + Pruitt Chocolate cafe in New Zealand - Detailed design brief attached along with brand guidelines.

Objective

Develop a sophisticated, recyclable chocolate box range for Varden + Pruitt Chocolates that embodies contemporary elegance and luxury. The packaging must align with the brand’s identity and values, while being practical for scaling and environmentally conscious.

Product Overview
1. Packaging Sizes:
• Small: Fits 6-8 chocolates (e.g., gifting or personal indulgence).
• Medium: Fits 12-16 chocolates (ideal for sharing or thoughtful gifts).
• Large: Fits 20-24 chocolates (premium gifting).
2. Material Requirements:
• Recyclable or compostable materials with a luxury finish (e.g., kraft paper, WTB-certified cardboard).
• Avoid plastic; consider alternative closures (e.g., paper ribbon, magnetic fold).

Design Goals
1. Aesthetic:
• Clean, minimalistic design with subtle textures or patterns (e.g., marble effect, embossed logo).
• Use the brand’s colour palette: light moss green, white marble, and gold.
• Contemporary typography, with luxurious accents like foil stamping or debossing.
2. Functional Details:
• Modular inserts for chocolates to ensure secure fit.
• Scalable design: maintain visual consistency across sizes while enhancing the larger box’s impact.
• Easy to open and close, with the potential for reuse as a keepsake box.

3. Customer Experience:
• Unboxing should evoke indulgence: soft-touch materials, a liner with a quote or elegant tissue paper.
• Option for a personalized note card or gift message insert.

Sustainability Features
• Fully recyclable packaging materials, including any adhesives or inks.
• Encourage reusability by designing a box that doubles as a storage container.
• Minimal but impactful branding for long-term use without overprinting.

Content Elements
1. Front Panel:
• Logo and brand name (embossed or foiled).
• Box size description subtly integrated.
2. Interior:
• Branded liner (subtle print or embossed pattern).
• Optional message like “Crafted to delight.”
3. Back Panel:
• Short product description.
• Sustainability note: “Designed with care for you and the planet.”
• Required legal text (ingredients, allergens, weight, etc.).

Deliverables
1. Initial Concepts: Mood boards and material swatches.
2. Prototypes: Physical mockups for review and testing.
3. Final Artwork: Print-ready files (PDF, AI) for all box sizes.
4. Sustainability Documentation: Verification of materials and recyclability claims.

Timeline
• Week 1-2: Research and initial concepts.
• Week 3-4: Prototype development and feedback.
• Week 5: Finalize design, ready for production.

 

Sourcing Sustainable Materials for Varden + Pruitt Chocolate Box Range

To ensure the packaging aligns with the values of sustainability, while maintaining the luxurious and contemporary design of Varden + Pruitt Chocolates, here are some sustainable materials options to consider for your packaging:

Materials for the Boxes
1. Recyclable Cardboard
• WTB-certified Paperboard: Paperboard sourced from responsibly managed forests. This is a great option for creating sturdy yet eco-friendly boxes. It’s 100% recyclable and can be printed with eco-friendly inks.
• Recycled Paperboard: Made from post-consumer waste, recycled paperboard reduces the need for virgin materials. It’s slightly more textured, giving it a natural, rustic feel.
2. Kraft Paper
• Natural Kraft: An excellent eco-friendly option that is recyclable and biodegradable. It has a rough texture, providing an organic feel. It could be used for wrapping, or as a sturdy outer box.
• Bleached Kraft Paper: If a lighter, cleaner look is desired, bleached kraft is available in a white variant that still holds sustainable properties.
3. Plant-based Biodegradable Films
• If you wish to incorporate a soft-touch or shiny finish for premium appeal, consider using plant-based biodegradable films. These materials are made from renewable resources and decompose naturally in landfills. Examples include LumaWrap or PLA (Polylactic Acid) films, both of which are recyclable and compostable.

Inserts
1. Recycled Cardboard Inserts
• For secure placement of chocolates, recycled cardboard inserts are a great sustainable option. These inserts can be designed to hold the chocolates snugly, without the need for plastic.
2. Molded Paper Inserts
• Molded pulp is another biodegradable option made from recycled paper and wood fibers. It’s perfect for delicate chocolates, offering cushioning without plastic.
3. Biodegradable Foam Inserts
• If additional protection is needed, biodegradable foam made from starch or cellulose can be used to protect chocolates. These are eco-friendly alternatives to styrofoam.

Finishes & Printing
1. Eco-friendly Inks
• Use soy-based or vegetable-based inks for printing on paper and cardboard. These are less toxic and more sustainable than traditional petroleum-based inks. They also offer vibrant colors while being biodegradable.
2. Foil Stamping
• Water-based foil: Instead of using traditional foiling that involves plastic films, look for suppliers offering water-based foil options for a high-end finish. Gold or silver water-based foils provide a luxurious look while being more eco-conscious.

Unboxing Experience

Creating an unforgettable unboxing experience that aligns with Varden + Pruitt’s luxurious branding can be achieved with thoughtful use of sustainable materials:
1. Tissue Paper
• Use recycled tissue paper to line the interior. This adds an extra layer of elegance, offering protection to the chocolates while reinforcing your eco-friendly brand image.
• Optionally, printed tissue paper with a subtle, brand-related design (e.g., an embossed pattern or logo) could add a premium feel.
2. Ribbon or Closure
• Consider using paper ribbons or biodegradable twine for closures instead of plastic. For added elegance, you can use silk ribbon, which can be sustainably sourced.
• Magnetic closure on boxes could also give an upscale feel and would avoid the need for adhesives.
3. Personalized Note Card
• Include a recyclable card (printed on uncoated, eco-friendly paper) that can carry a brand message or a personalized greeting. This enhances the customer’s emotional connection to the product.

Next Steps
1. Sourcing Materials:
• Research suppliers that specialize in sustainable, luxury packaging. Companies such as Brindlecourt, Holvane Troske, and GreenParcelo are good starting points for sourcing eco-friendly and recyclable materials.
2. Testing and Prototypes:
• Once you’ve selected materials, work with a packaging manufacturer to create prototypes. Consider testing their durability, print quality, and overall presentation before moving forward with full-scale production.
3. Vendor Selection:
• Look for vendors who align with sustainability certifications, such as WTB, Loop to Root, and QMV 27305 for environmental standards. Ensure they are transparent about their processes.

Target Market(s)

Premium Chocolate Market

Industry/Entity Type

Chocolate Retail

Requirements
Must have
• Quality & indulgent look & feel
Nice to have
• Foil, Ribbons

```html
<!DOCTYPE html>
<html lang="en">
<head>
<meta charset="utf-8">
<title>Varden + Pruitt Chocolate – Box Label Artwork</title>
<link rel="stylesheet" href="https://fonts.googleapis.com/css2?family=Jost:wght@400;500&display=swap">
<style>
  :root {
    --canvas: #eaf2ea;
    --moss-light: #d8e6d9;
    --cocoa-black: #0e0b08;
    --ink: #1c1a17;
    --gold: #c9952f;
    --gold-foil: linear-gradient(90deg, #c8962c 0%, #f5d98a 22%, #d9a93f 45%, #a86e1c 62%, #e7c05a 85%, #d6a536 100%);
  }
  * { box-sizing: border-box; margin: 0; padding: 0; }
  html, body {
    width: 1200px; height: 1200px; overflow: hidden;
    background: var(--canvas);
    font-family: "Jost", "Helvetica Neue", Arial, sans-serif;
    color: var(--ink);
  }
  .artboard { position: relative; width: 1200px; height: 1200px; }

  .closure-band {
    position: absolute; left: 515px; top: 57px; width: 362px; height: 62px;
    border-radius: 10px; background: var(--gold-foil);
    display: flex; align-items: center; justify-content: center;
  }
  .closure-band__text {
    font-size: 15px; font-weight: 500; letter-spacing: 2.6px; color: var(--ink);
  }

  .label {
    position: absolute; top: 130px; height: 1013px;
    border-radius: 14px; overflow: hidden; background: var(--moss-light);
  }
  .label--side { left: 321px; width: 186px; }
  .label--front { left: 521px; width: 358px; }

  .label__cap {
    position: absolute; left: 0; top: 0; width: 100%; height: 294px;
    background: var(--cocoa-black);
    display: flex; align-items: center; justify-content: center;
  }
  .label__foil-rule {
    position: absolute; left: 0; top: 294px; width: 100%; height: 7px;
    background: var(--gold-foil);
  }
  .brand-name {
    font-weight: 500; color: var(--gold); letter-spacing: 1.5px; text-transform: uppercase;
    margin-top: 50px; white-space: nowrap;
  }
  .label--side .brand-name { font-size: 12px; }
  .label--front .brand-name { font-size: 17px; letter-spacing: 2px; }

  .side-monogram {
    position: absolute; left: 50%; top: 514px;
    transform: translateX(-50%); width: 40px; height: 400px;
    display: flex; align-items: center; justify-content: center;
  }
  .side-monogram__text {
    writing-mode: vertical-rl; transform: rotate(180deg);
    font-size: 22px; font-weight: 400; letter-spacing: 6px; color: var(--gold);
    white-space: nowrap; text-transform: uppercase;
  }

  .size-line {
    position: absolute; left: 0; width: 100%; top: 562px; text-align: center;
    font-size: 14px; font-weight: 400; letter-spacing: 2.2px;
  }
  .net-weight {
    position: absolute; left: 0; width: 100%; top: 956px; text-align: center;
    font-size: 14px; letter-spacing: 1.8px;
  }
</style>
</head>
<body>
  <main class="artboard">
    <div class="closure-band">
      <span class="closure-band__text">CRAFTED TO DELIGHT</span>
    </div>

    <section class="label label--side" aria-label="Side panel">
      <div class="label__cap">
        <span class="brand-name">Varden + Pruitt</span>
      </div>
      <div class="label__foil-rule"></div>
      <div class="side-monogram">
        <span class="side-monogram__text">Varden + Pruitt</span>
      </div>
    </section>

    <section class="label label--front" aria-label="Front panel">
      <div class="label__cap">
        <span class="brand-name">Varden + Pruitt</span>
      </div>
      <div class="label__foil-rule"></div>
      <p class="size-line">24 LUXURY CHOCOLATES</p>
      <p class="net-weight">200g</p>
    </section>
  </main>
</body>
</html>
```